Flyer Design Project

We need a flyer for a monthly event that we will be having. The flyer needs to be editable in either adobe illustrator or photoshop so that we can change the details such as the date if needed... Preferable in vector art.

Name of Event : Sandalmania

Price of Tickets: $15 Tickets- Entry fee ensures a pair of thongs upon leaving, drink specials all night and priority entry.

WHEN- FEB 20th
WHERE- Velvet Loft
DJ: Tessa Harlow
web: www.velvetloftbar.com.au
ph: 9146 3705

Drink specials from 7-9pm
$3 Pots
$4 basics
$4 kelvanos

$1 pizza from 8pm-10pm

FREE PAIR OF THONGS ON DEPARTURE

Drink specials continue throughout the night

Open 7pm-3am
Updates

Hi there,

Just to be clear, a pair of thongs isĀ referringĀ to flip flops or sandals (not underwear)... thanks

Target Market(s)

University Students 18-24 years old

Industry/Entity Type

Apartment

Requirements
Must have
• must have our logo

```html
<!DOCTYPE html>
<html lang="en">
<head>
<meta charset="utf-8">
<title>Sandalmania Flyer</title>
<link rel="stylesheet" href="https://fonts.googleapis.com/css2?family=Titan+One&family=Cabin:wght@700&family=Arimo:wght@700&display=swap">
<style>
  :root {
    --page: #ffffff;
    --sky: #2aa3e0;
    --sky-deep: #1b86c8;
    --sandal-green: #9ccf3a;
    --sandal-red: #d9362b;
    --pale-sky: #c9ddf2;
    --pale-green: #d8e6b0;
    --pale-coral: #e9c3b4;
    --ink: #111111;
    --white: #ffffff;
    --grey-copy: #4a4f57;
  }
  html, body {
    margin: 0;
    width: 1200px;
    height: 817px;
    overflow: hidden;
    background: var(--page);
  }
  .canvas {
    position: relative;
    width: 1200px;
    height: 817px;
  }
  .flyer {
    position: absolute;
    top: 22px;
    width: 546px;
    height: 768px;
    overflow: hidden;
  }
  .flyer--front { left: 20px; }
  .flyer--back { left: 630px; }

  .sandal-photo {
    position: absolute;
    inset: 0;
  }
  .flyer--front .sandal-photo {
    background:
      radial-gradient(ellipse 60% 42% at 55% 52%, var(--sandal-green) 0 55%, transparent 72%),
      radial-gradient(ellipse 20% 14% at 40% 46%, var(--sandal-red) 0 50%, transparent 80%),
      linear-gradient(160deg, var(--sky) 0%, var(--sky-deep) 100%);
  }
  .flyer--back .sandal-photo {
    background:
      radial-gradient(ellipse 60% 42% at 55% 52%, var(--pale-green) 0 55%, transparent 72%),
      radial-gradient(ellipse 22% 16% at 75% 28%, var(--pale-coral) 0 50%, transparent 80%),
      linear-gradient(160deg, #d3e4f5 0%, var(--pale-sky) 100%);
  }

  .outlined {
    font-family: "Titan One", "Arial Black", sans-serif;
    color: var(--white);
    text-shadow:
      -2px -2px 0 var(--ink), 2px -2px 0 var(--ink),
      -2px 2px 0 var(--ink), 2px 2px 0 var(--ink),
      0 -2px 0 var(--ink), 0 2px 0 var(--ink),
      -2px 0 0 var(--ink), 2px 0 0 var(--ink);
    margin: 0;
    position: absolute;
    line-height: 1.1;
  }

  /* front */
  .front-title { left: 30px; top: 38px; font-size: 44px; }
  .front-date { left: 30px; top: 96px; font-size: 36px; }
  .front-hours { left: 30px; top: 148px; font-size: 24px; }
  .venue-name {
    position: absolute;
    left: 0; right: 0;
    top: 628px;
    text-align: center;
    font-family: "Titan One", "Arial Black", sans-serif;
    font-size: 44px;
    color: var(--white);
    margin: 0;
  }
  .front-web { left: 0; right: 0; top: 704px; text-align: center; font-size: 23px; }

  /* back */
  .back-block { position: absolute; left: 0; right: 0; text-align: center; margin: 0; }
  .back-title { left: 0; right: 0; text-align: center; top: 38px; font-size: 28px; }
  .back-offer { left: 0; right: 0; text-align: center; top: 96px; font-size: 30px; line-height: 1.15; letter-spacing: 0.5px; }
  .ticket-copy {
    top: 190px;
    font-family: "Cabin", "Gill Sans", sans-serif;
    font-weight: 700;
    font-size: 28px;
    line-height: 36px;
    color: var(--grey-copy);
    padding: 0 40px;
  }
  .dj-name { left: 0; right: 0; text-align: center; top: 352px; font-size: 34px; }
  .drink-list {
    top: 420px;
    list-style: none;
    padding: 0;
    font-family: "Cabin", "Gill Sans", sans-serif;
    font-weight: 700;
    font-size: 26px;
    line-height: 36px;
    color: var(--grey-copy);
  }
  .drink-note {
    top: 616px;
    font-family: "Cabin", "Gill Sans", sans-serif;
    font-weight: 700;
    font-size: 16px;
    color: var(--grey-copy);
  }
  .phone {
    top: 654px;
    font-family: "Arimo", Arial, sans-serif;
    font-weight: 700;
    font-size: 34px;
    color: var(--ink);
  }
  .back-web { left: 0; right: 0; text-align: center; top: 704px; font-size: 23px; }
</style>
</head>
<body>
<main class="canvas">
  <section class="flyer flyer--front">
    <div class="sandal-photo" role="img" aria-label="Close-up photo of a green flip flop with red and coral flower prints on a blue background"></div>
    <h1 class="outlined front-title">Sandalmania</h1>
    <p class="outlined front-date">February 20th</p>
    <p class="outlined front-hours">7pm - 3am</p>
    <p class="venue-name">Velvet Loft</p>
    <p class="outlined front-web">www.velvetloftbar.com.au</p>
  </section>

  <section class="flyer flyer--back">
    <div class="sandal-photo" role="img" aria-label="Faded photo of a flip flop with flower prints on a pale blue background"></div>
    <h2 class="outlined back-title">Sandalmania</h2>
    <p class="outlined back-offer">FREE PAIR OF THONGS<br>ON DEPARTURE</p>
    <p class="back-block ticket-copy">Tickets: $15 Tickets- Entry fee ensures a pair of thongs upon leaving, drink specials all night and priority entry.</p>
    <p class="outlined dj-name">DJ: Tessa Harlow</p>
    <ul class="back-block drink-list">
      <li>Drink specials from 7-9pm</li>
      <li>$3 Pots</li>
      <li>$4 basics</li>
      <li>$4 kelvanos</li>
      <li>$1 pizza from 8pm-10pm</li>
    </ul>
    <p class="back-block drink-note">Drink specials continue throughout the night</p>
    <p class="back-block phone">9146 3705</p>
    <p class="outlined back-web">www.velvetloftbar.com.au</p>
  </section>
</main>
</body>
</html>
```